Web Design Project (Mente Lumo)

We are going to do a therapy template to a psychologist. The site already exists, adress: www.mentelumo.net. So, its a total redesign job. I'm from Brazil, the language is PT-BR, so I'm gonna translate what you think be necessary. You can use the current structure from the website as a base to the new design. Check this template to see what I usually like: http://www.layoutkiosk.example/demo/51937.html
Updates

I'm waiting for new creative designs. The 'structure' image is just for 'pb'.

Requirements
Must have
• We need a modern menu, it should use a cool font style and make some kind of effect and little noise when the user pass over with the mouse (FLASH/HTML 5). The main page must emphasize the fact that we offer online treatment, like a picture or frame saying "Online Treatment, click here". It must also show the therapist picture and her name. The colors need to pass a tranquility feeling. The clinic telephone must always be present, doesn't matter which page the user is. The website must adapt to any resolution above 1024x768, crossbrowsing and accept javascript (I'll use www.agendrix.example, so its necessary embed code)
Nice to have
• I would appreciate if there was some kind of slow background animation, passing behind the text using the transparency.
Should not have
• Can't take too long to load, and won't have news or blog

```html
<!DOCTYPE html>
<html lang="en">
<head>
<meta charset="utf-8">
<title>Mente Lumo – Cognitive Therapy</title>
<link rel="stylesheet" href="https://fonts.googleapis.com/css2?family=Signika:wght@300;400;600&family=Ubuntu+Condensed&display=swap">
<style>
:root{
  --teal:#2596a8;
  --teal-dark:#1f7f8f;
  --sky:#a9dbe4;
  --sky-light:#d3ecf1;
  --sky-band:#8fd0dc;
  --tab:#5fc3d4;
  --green:#6ab532;
  --green-dark:#4c8f1f;
  --ink:#333;
  --paper:#f1f2f2;
  --white:#fff;
}
*{margin:0;padding:0;box-sizing:border-box}
html,body{width:1200px;height:1030px;overflow:hidden}
body{position:relative;background:var(--paper);font-family:"Ubuntu Condensed",sans-serif;color:var(--ink)}
.abs{position:absolute}

/* header */
.site-header{left:0;top:0;width:1200px;height:80px;background:linear-gradient(#fff,#eef4f5);border-bottom:3px solid #8cc9d4;z-index:3}
.brand{left:145px;top:18px;display:flex;align-items:center;gap:10px;font-family:"Signika",sans-serif;font-weight:600;font-size:30px;color:#8fc54a}
.brand-dot{width:30px;height:30px;border-radius:50%;background:#b8e1e9}
.main-nav{left:0;top:0;height:80px;width:1200px;font-family:"Signika",sans-serif;font-size:17px;font-weight:600}
.main-nav a{position:absolute;top:33px;color:var(--teal);text-decoration:none}
.nav-tab{left:468px;top:0;width:86px;height:97px;z-index:4}
.main-nav a.active{color:#fff;z-index:5}

/* hero */
.hero{left:0;top:80px;width:1200px;height:383px;background:linear-gradient(#9fd6e0,#d6eef2)}
.hero-panel{left:145px;top:50px;width:910px;height:333px;background:rgba(255,255,255,.35)}
.hero-title{left:182px;top:165px;font-family:"Signika",sans-serif;font-weight:600;font-size:41px;color:var(--teal);text-shadow:0 1px 0 rgba(255,255,255,.6)}
.hero-text{left:183px;top:222px;width:476px;font-size:12.5px;line-height:16px;color:var(--teal);text-align:justify}
.hero-list{left:183px;top:297px;list-style:none;font-size:12.5px;line-height:18.5px;color:var(--teal)}
.hero-list li::before{content:"";display:inline-block;width:6px;height:6px;border-radius:50%;background:var(--teal);margin-right:7px;vertical-align:1px}
.btn-learn{left:181px;top:385px;width:163px;height:44px;border-radius:4px;background:linear-gradient(#8fd050,#5aa826);border:1px solid var(--green-dark);font-family:"Signika",sans-serif;font-weight:600;font-size:23px;color:#2e5f12;display:flex;align-items:center;justify-content:center;box-shadow:0 2px 3px rgba(0,0,0,.2)}
.therapist-photo{left:720px;top:97px;width:285px;height:366px;background:linear-gradient(#7a7a7a,#c8c8c8);border-radius:140px 140px 0 0}
.hero-caption{left:667px;top:413px;width:388px;height:50px;background:rgba(143,208,220,.92);color:#fff;font-family:"Signika",sans-serif;font-size:22px;display:flex;align-items:center;justify-content:center}

/* content */
.content{left:0;top:463px;width:1200px;height:480px;background:repeating-linear-gradient(90deg,#eceeee 0 2px,#f4f5f5 2px 4px)}
.about-photo{left:147px;top:508px;width:138px;height:144px;border:4px solid #fff;box-shadow:0 0 0 1px #ccc;background:linear-gradient(#c9b27a,#7ca6cf)}
.about-name{left:153px;top:660px;font-family:"Signika",sans-serif;font-size:14px;color:var(--green)}
.about-title{left:305px;top:505px;font-family:"Signika",sans-serif;font-size:23px;color:#333}
.about-text{font-size:12.3px;line-height:16.2px;text-align:justify;color:#444}
.about-text p{margin-bottom:10px}

/* contact cards */
.card{left:727px;width:323px;background:linear-gradient(#fff,#f1f1f1);border-bottom:1px solid #ccd}
.card h3{position:absolute;left:125px;font-family:"Signika",sans-serif;font-weight:400;font-size:21px;color:#333}
.card .phones{position:absolute;left:125px;top:51px;font-family:"Signika",sans-serif;font-weight:600;font-size:15px;line-height:20px;color:#222}
.card p{position:absolute;left:125px;width:186px;font-size:12px;line-height:12px;text-align:justify;color:#444}
.card .btn-small{position:absolute;left:124px;width:79px;height:25px;border-radius:13px;background:linear-gradient(#a8dd6c,#62ad2a);border:1px solid var(--green-dark);font-size:11px;color:#2e5f12;display:flex;align-items:center;justify-content:center}
.clip{width:10px;height:52px;z-index:2}
.map-icon{left:757px;top:806px;width:82px;height:70px;border-radius:6px;background:linear-gradient(135deg,#3c8ed6,#a8c9e6)}

/* footer */
.site-footer{left:0;top:943px;width:1200px;height:87px;background:repeating-linear-gradient(90deg,#c3e4ea 0 2px,#d3ecf0 2px 4px);border-top:1px solid #b7dbe2;font-family:"Signika",sans-serif;font-size:14px;color:var(--teal-dark)}
.copyright{left:147px;top:30px}
.address{left:807px;top:30px;line-height:17px}
</style>
</head>
<body>

<header class="site-header abs">
  <div class="brand abs"><span class="brand-dot"></span>Mente Lumo</div>
</header>
<svg class="nav-tab abs" viewBox="0 0 86 97" aria-hidden="true">
  <path d="M0 0H86V84L43 97L0 84Z" fill="#5fc3d4"/>
  <path d="M0 0H86V80H0Z" fill="#8bd3e0" opacity=".35"/>
</svg>
<nav class="main-nav abs" style="z-index:5">
  <a class="active" href="#" style="left:493px">Home</a>
  <a href="#" style="left:568px">Treatments</a>
  <a href="#" style="left:681px">Questions</a>
  <a href="#" style="left:783px">Ask the expert</a>
  <a href="#" style="left:912px">Location</a>
  <a href="#" style="left:1001px">Contact</a>
</nav>

<section class="hero abs">
  <div class="hero-panel abs"></div>
</section>
<h1 class="hero-title abs">O que e terapia cognitiva</h1>
<p class="hero-text abs">Sed ut perspiciatis unde omnis iste natus error sit voluptatem accusantium doloremque laudantium, totam rem aperiam, eaque ipsa quae ab illo inventore veritatis et quasi architecto beatae vitae dicta sunt explicabo. Nemo enim ipsam voluptatem quia voluptas sit aspernatur aut odit aut fugit, sed quia consequuntur magni dolores eos qui ratione voluptatem sequi nesciunt.</p>
<ul class="hero-list abs">
  <li>Neque porro quisquam est qui dolorem ipsum.</li>
  <li>Ut enim ad minima veniam.</li>
  <li>Sed ut perspiciatis unde omnis iste natus error sit.</li>
  <li>Lorem ipsum dolor sit amet consectetur adipisicing.</li>
</ul>
<a class="btn-learn abs">Learn more</a>
<div class="therapist-photo abs" role="img" aria-label="Portrait photo of the therapist"></div>
<div class="hero-caption abs">Voluptatem accusantium doloremque</div>

<main class="content abs"></main>
<div class="about-photo abs" role="img" aria-label="Photo of psychologist Lia Moraes"></div>
<div class="about-name abs">Psicologa Lia Moraes</div>
<h2 class="about-title abs">About us</h2>
<div class="about-text abs" style="left:305px;top:541px;width:397px">
  <p>The Cognitive Therapy is as a method of interpreting mental contents and processes cognitions, and its influence on daily life. The behavior and emotion come after cognitive processing. It is vital to know your thoughts on them under control, so we can nourish them, expand them, reduce them or reject them.</p>
  <p>Every mental disorder originates in thought. The Cognitive Therapy education through the search of his emotional balance. To do so, establish strategies is of real importance to the resolution of complaints.</p>
</div>
<div class="about-text abs" style="left:148px;top:686px;width:554px">
  <p>When the individual has a balanced operation, it can have a greater resistance facing the adversities that happen in the day-to-day. To understand the nature of a disease, we must understand the nature of the individual s relationships with the world that is around them.</p>
  <p>Arnold Brisk, creator of Cognitive Therapy, states that cognition, not emotion, is the essential factor in depression, which Brisk describes as thought disorder, and not emotional. He claims that the negativity was not a depressive symptom, but has a central role in the installation and maintenance of the disorder. The sessions and the therapeutic process are semi-structured, involving tasks between sessions, and is focused on the specific problems of patients and the therapeutic goals.</p>
</div>
<div class="about-text abs" style="left:145px;top:831px;width:557px">
  <p>Cognitive therapy is teaching, because his goal is not only to help the patient in their problems, but to educate you use the tool instrumental cognitive and behavioral order to realize that the real world and respond in a functional way. There are physical benefits when the mind is positive. According to Daniel Sorel and Roland Orwin, it strengthens the immune system and increases longevity.</p>
</div>

<section class="card abs" style="top:507px;height:127px">
  <svg class="abs" style="left:31px;top:22px" width="80" height="80" viewBox="0 0 80 80" aria-hidden="true">
    <defs><radialGradient id="phoneBg" cx=".4" cy=".3" r=".8"><stop offset="0" stop-color="#7fd8f5"/><stop offset="1" stop-color="#1494cf"/></radialGradient></defs>
    <circle cx="40" cy="40" r="38" fill="url(#phoneBg)"/>
    <path d="M28 22c3-2 6 4 7 7 1 2-3 4-2 6 2 5 6 9 11 11 2 1 4-3 6-2 3 1 9 4 7 7-2 4-6 6-10 5-11-3-20-12-23-23-1-4 1-8 4-11z" fill="#fff"/>
  </svg>
  <h3 style="top:19px">Telephone</h3>
  <div class="phones">3510-4426<br>9184-2270<br>7765-0318</div>
</section>
<section class="card abs" style="top:641px;height:127px">
  <svg class="abs" style="left:28px;top:22px" width="84" height="78" viewBox="0 0 84 78" aria-hidden="true">
    <path d="M38 4C18 4 3 17 3 33c0 9 5 17 13 22l-3 18 17-13c3 1 5 1 8 1 20 0 35-13 35-28S58 4 38 4z" fill="#5cc6ef"/>
    <circle cx="60" cy="48" r="16" fill="#1d86c4"/>
    <circle cx="60" cy="40" r="2.6" fill="#fff"/><rect x="57.5" y="45" width="5" height="13" rx="1.5" fill="#fff"/>
  </svg>
  <h3 style="top:19px">Online Treatment</h3>
  <p style="top:49px">Sed ut perspiciatis unde omnis iste natus error sit voluptatem.</p>
  <div class="btn-small" style="top:78px">CLICK HERE</div>
</section>
<section class="card abs" style="top:775px;height:125px">
  <h3 style="top:21px">Our map</h3>
  <p style="top:50px">Sed ut perspiciatis unde omnis iste natus error sit voluptatem.</p>
  <div class="btn-small" style="top:79px">CLICK HERE</div>
</section>
<div class="map-icon abs" role="img" aria-label="Illustration of a folded map with a compass"></div>
<svg class="clip abs" style="left:740px;top:610px" viewBox="0 0 10 52" aria-hidden="true"><rect x="2" y="0" width="6" height="52" rx="3" fill="#4a8fa0"/><circle cx="5" cy="5" r="4" fill="#2f6f80"/><circle cx="5" cy="47" r="4" fill="#2f6f80"/></svg>
<svg class="clip abs" style="left:1028px;top:610px" viewBox="0 0 10 52" aria-hidden="true"><rect x="2" y="0" width="6" height="52" rx="3" fill="#4a8fa0"/><circle cx="5" cy="5" r="4" fill="#2f6f80"/><circle cx="5" cy="47" r="4" fill="#2f6f80"/></svg>
<svg class="clip abs" style="left:740px;top:744px" viewBox="0 0 10 52" aria-hidden="true"><rect x="2" y="0" width="6" height="52" rx="3" fill="#4a8fa0"/><circle cx="5" cy="5" r="4" fill="#2f6f80"/><circle cx="5" cy="47" r="4" fill="#2f6f80"/></svg>
<svg class="clip abs" style="left:1028px;top:744px" viewBox="0 0 10 52" aria-hidden="true"><rect x="2" y="0" width="6" height="52" rx="3" fill="#4a8fa0"/><circle cx="5" cy="5" r="4" fill="#2f6f80"/><circle cx="5" cy="47" r="4" fill="#2f6f80"/></svg>

<footer class="site-footer abs">
  <div class="copyright abs">© Copyright 2012 - All rights reserved</div>
  <div class="address abs">Clearwater Hill Street, 145,<br>5th floor, room 52 - Center - Vila Serena, SP</div>
</footer>

</body>
</html>
```